Body therapist needs a business card

I need a card for my business which is teaching trainings in body therapy, the company is called Wellacombe Educational Group. I teach to massage therapists around Australia, South East Asia and the USA. I am attaching my logo which will guide you as to what colours I would like to have you consider. Please consult my website to find out more about what I do. www.kinetrova.com.au

My name is Gareth Wellacombe. My phone number is (03) 9157 2618 or 0412573086. email is info@kinetrova.com.au

```html
<!DOCTYPE html>
<html lang="en">
<head>
<meta charset="utf-8">
<title>Wellacombe Educational Group – Business Card</title>
<link rel="stylesheet" href="https://fonts.googleapis.com/css2?family=Lato:wght@400;700&family=Oswald:wght@500&display=swap">
<style>
  :root {
    --backdrop: #2b2b2d;
    --card: #121212;
    --card-edge: #1c1c1c;
    --accent-lime: #d4e00f;
    --brand-brown: #8a4a12;
    --text-light: #e6e6e6;
    --divider: #6a6a6a;
  }
  * { margin: 0; padding: 0; box-sizing: border-box; }
  html, body {
    width: 1200px;
    height: 900px;
    overflow: hidden;
    background: var(--backdrop);
  }
  .stage {
    position: relative;
    width: 1200px;
    height: 900px;
  }
  .card {
    position: absolute;
    left: 300px;
    width: 600px;
    height: 340px;
    background: linear-gradient(160deg, var(--card-edge), var(--card));
    border-bottom: 9px solid var(--accent-lime);
    overflow: hidden;
  }
  .card--front { top: 70px; }
  .card--back { top: 480px; }

  /* Front */
  .brand {
    position: absolute;
    left: 0;
    right: 0;
    top: 122px;
    text-align: center;
  }
  .brand__name {
    font-family: "Lato", sans-serif;
    font-weight: 400;
    font-size: 32px;
    line-height: 1.2;
    color: var(--brand-brown);
    letter-spacing: 0.5px;
  }

  /* Back */
  .holder {
    position: absolute;
    left: 70px;
    top: 120px;
    font-family: "Oswald", sans-serif;
    font-weight: 500;
    font-size: 26px;
    text-transform: uppercase;
    color: var(--brand-brown);
    letter-spacing: 0.3px;
  }
  .divider {
    position: absolute;
    left: 320px;
    top: 110px;
    width: 1px;
    height: 78px;
    background: var(--divider);
  }
  .contacts {
    position: absolute;
    left: 345px;
    top: 112px;
    list-style: none;
    font-family: "Lato", sans-serif;
    font-size: 16px;
    color: var(--text-light);
  }
  .contacts li {
    display: flex;
    align-items: center;
    gap: 8px;
    height: 24px;
  }
  .contacts svg { width: 13px; height: 13px; fill: var(--brand-brown); flex: none; }
  .address {
    position: absolute;
    left: 70px;
    top: 250px;
    font-family: "Lato", sans-serif;
    font-size: 17px;
    color: var(--text-light);
    letter-spacing: 0.2px;
  }
</style>
</head>
<body>
<main class="stage">
  <section class="card card--front" aria-label="Card front">
    <div class="brand">
      <p class="brand__name">Wellacombe<br>Educational Group</p>
    </div>
  </section>

  <section class="card card--back" aria-label="Card back">
    <h1 class="holder">Gareth Wellacombe</h1>
    <span class="divider"></span>
    <ul class="contacts">
      <li>
        <svg viewBox="0 0 16 16" aria-hidden="true"><path d="M3 1h3l1.5 4-2 1.3a9 9 0 0 0 4.2 4.2L11 8.5l4 1.5v3a2 2 0 0 1-2 2A12 12 0 0 1 1 3a2 2 0 0 1 2-2z"/></svg>
        +61 (03) 9157 2618
      </li>
      <li>
        <svg viewBox="0 0 16 16" aria-hidden="true"><path d="M1 3h14v10H1z M1 3l7 6 7-6" stroke="#121212" stroke-width="1.2"/></svg>
        info@kinetrova.com.au
      </li>
      <li>
        <svg viewBox="0 0 16 16" aria-hidden="true"><circle cx="8" cy="8" r="7"/><path d="M1 8h14M8 1c-3 3.5-3 10.5 0 14M8 1c3 3.5 3 10.5 0 14" stroke="#121212" stroke-width="1" fill="none"/></svg>
        www.kinetrova.com.au
      </li>
    </ul>
    <p class="address">P.O. Box 2847, Ringwood East Victoria, 3135 Australia</p>
  </section>
</main>
</body>
</html>
```